Stationery Design Project

We need a stationary design (business card, logo, letterhead) for a new company called "Meridel Kestrova".
We provide software and consulting services to improve business efficiency & increase team engagement.
We focus on workflow automation, business social networking software and collaboration and communication tools built on mobile platforms.
Updates

Target Market(s)

Business with multi-site,young, mobile workforces e.g Retailers, Hospitality

Industry/Entity Type

Communication

Requirements
Must have
• Letterhead to include;
Business Address: 17 Wendle St, Corvath Vale, NSW 2100
ABN : 48 615 207 392

```html
<!DOCTYPE html>
<html lang="en">
<head>
<meta charset="utf-8">
<title>Meridel Kestrova — Stationery</title>
<link rel="stylesheet" href="https://fonts.googleapis.com/css2?family=Michroma&family=Arimo:ital,wght@0,400;0,700;1,700&display=swap">
<style>
  :root{
    --teal:#1fa9a5;
    --teal-deep:#0e6e6a;
    --ink:#1d1d1d;
    --paper:#ffffff;
    --ground:#e4e6e7;
    --card-dark:#2b2725;
    --card-dark-edge:#151312;
    --muted:#cfcfcf;
    --watermark:#eef1f1;
  }
  *{box-sizing:border-box;margin:0;padding:0}
  html,body{width:1200px;height:1200px;overflow:hidden}
  body{background:var(--ground);position:relative;font-family:"Arimo",Arial,sans-serif;color:var(--ink)}

  .wordmark{font-family:"Michroma",sans-serif;text-transform:uppercase;color:var(--teal);line-height:1.15;font-weight:400}

  /* Letterhead */
  .letterhead{position:absolute;left:50px;top:147px;width:640px;height:905px;background:var(--paper);box-shadow:0 4px 18px rgba(0,0,0,.18);overflow:hidden}
  .letterhead__tab{position:absolute;left:0;top:0;width:22px;height:75px;background:var(--teal)}
  .letterhead__logo{position:absolute;left:34px;top:30px;font-size:17px}
  .letterhead__watermark{position:absolute;left:250px;top:640px;font-size:58px;color:var(--watermark);line-height:1.05}
  .letterhead__footbar{position:absolute;left:0;top:770px;width:18px;height:135px;background:var(--teal)}
  .letterhead__company{position:absolute;left:30px;top:782px;font-weight:700;font-style:italic;font-size:15px;text-transform:uppercase;letter-spacing:.2px}
  .letterhead__rule{position:absolute;left:18px;top:803px;width:235px;height:12px}
  .letterhead__abn{position:absolute;left:95px;top:817px;color:var(--teal);font-size:11px}
  .letterhead__address{position:absolute;left:30px;top:840px;font-size:9.5px}
  .letterhead__contacts{position:absolute;left:30px;top:862px;font-size:8.5px;line-height:1.25;list-style:none}
  .letterhead__mark{position:absolute;left:300px;top:790px;font-size:17px;color:var(--teal-deep)}

  /* Cards */
  .card{position:absolute;left:740px;width:410px;height:228px;overflow:hidden;box-shadow:0 3px 12px rgba(0,0,0,.2)}
  .card--dark{background:radial-gradient(ellipse at 45% 40%,#4a4440 0%,var(--card-dark) 55%,var(--card-dark-edge) 100%);color:#fff}
  .card--light{background:var(--paper);color:var(--ink)}
  .card--f1{top:60px}.card--b1{top:320px}.card--f2{top:580px}.card--b2{top:840px}

  .card__edge{position:absolute;top:12px;width:7px;height:168px;background:var(--teal)}
  .card__edge--left{left:0}.card__edge--right{right:0}
  .card__baseline{position:absolute;left:0;right:0;top:178px;height:2px;background:var(--teal)}
  .card__logo-centre{position:absolute;left:0;right:0;top:76px;text-align:center;font-size:22px}
  .card__services{position:absolute;left:60px;right:40px;top:160px;display:flex;justify-content:space-between;font-size:8.5px;list-style:none}
  .card__services li::before{content:"• "}
  .card--dark .card__services{color:var(--muted)}

  .card__logo-small{position:absolute;left:24px;top:28px;font-size:12px}
  .card--dark .card__logo-small{color:#fff}
  .card--light .card__logo-small{color:var(--ink)}
  .card__name{position:absolute;left:24px;top:88px;font-weight:700;font-style:italic;font-size:19px;text-transform:uppercase}
  .card__role-bar{position:absolute;left:0;top:112px;width:400px;height:16px}
  .card__role{position:absolute;left:105px;top:113px;font-size:10px;color:var(--teal)}
  .card--dark .card__role{color:#fff}
  .card__contacts{position:absolute;left:24px;top:138px;font-size:9.5px;list-style:none;line-height:1.5}
  .card__contacts li{display:flex;align-items:center;gap:6px}
  .card__contacts li.gap{margin-bottom:6px}
  .card__contacts svg{width:9px;height:9px;flex:none}
  .card--dark .card__contacts{color:#e6e6e6}
  .card__mark{position:absolute;left:232px;top:60px;font-size:20px;color:var(--teal);text-align:left}
</style>
</head>
<body>

<section class="letterhead" aria-label="Letterhead">
  <div class="letterhead__tab"></div>
  <div class="letterhead__logo wordmark">Meridel<br>Kestrova</div>
  <div class="letterhead__watermark wordmark" aria-hidden="true">Meridel<br>Kestrova</div>

  <div class="letterhead__footbar"></div>
  <div class="letterhead__company">Meridel Kestrova</div>
  <svg class="letterhead__rule" viewBox="0 0 235 12" preserveAspectRatio="none" aria-hidden="true">
    <polygon points="0,0 225,0 235,6 225,12 0,12" fill="var(--teal)"/>
  </svg>
  <div class="letterhead__abn">ABN : 48 615 207 392</div>
  <div class="letterhead__address">17 Wendle St, Corvath Vale, NSW 2100</div>
  <ul class="letterhead__contacts">
    <li>mobile: +61 2 8150 4417</li>
    <li>telephone: +61 455 302 918</li>
    <li>email: arlo.penhallow@meridelkestrova.com</li>
    <li>web: www.meridelkestrova.com</li>
  </ul>
  <div class="letterhead__mark wordmark">Meridel<br>Kestrova</div>
</section>

<!-- Dark card front -->
<section class="card card--dark card--f1" aria-label="Business card front, dark">
  <div class="card__edge card__edge--left"></div>
  <div class="card__edge card__edge--right"></div>
  <div class="card__logo-centre wordmark">Meridel Kestrova</div>
  <ul class="card__services"><li>Business Service</li><li>Business Service</li><li>Business Service</li></ul>
  <div class="card__baseline"></div>
</section>

<!-- Dark card back -->
<section class="card card--dark card--b1" aria-label="Business card back, dark">
  <div class="card__logo-small wordmark">Meridel<br>Kestrova</div>
  <div class="card__name">Arlo Penhallow</div>
  <svg class="card__role-bar" viewBox="0 0 400 16" preserveAspectRatio="none" aria-hidden="true">
    <polygon points="0,0 150,0 160,8 150,16 0,16" fill="var(--teal)"/>
    <rect x="160" y="7" width="240" height="1.5" fill="var(--teal)"/>
  </svg>
  <div class="card__role">Director</div>
  <ul class="card__contacts">
    <li class="gap"><svg viewBox="0 0 10 10"><path d="M5 0C3 0 1.6 1.5 1.6 3.3 1.6 6 5 10 5 10s3.4-4 3.4-6.7C8.4 1.5 7 0 5 0zm0 4.6a1.3 1.3 0 110-2.6 1.3 1.3 0 010 2.6z" fill="currentColor"/></svg>17 Wendle St, Corvath Vale, NSW 2100</li>
    <li><svg viewBox="0 0 10 10"><rect x="2.5" y="0" width="5" height="10" rx="1" fill="currentColor"/></svg>+61 2 8150 4417</li>
    <li><svg viewBox="0 0 10 10"><path d="M2 0l2 2.5-1 1.2c.7 1.4 1.8 2.5 3.2 3.2l1.2-1L10 8 8.6 10C4 9.4.6 6 0 1.4z" fill="currentColor"/></svg>+61 455 302 918</li>
    <li><svg viewBox="0 0 10 10"><rect x="0" y="2" width="10" height="6.5" fill="none" stroke="currentColor"/><path d="M0 2l5 3.5L10 2" fill="none" stroke="currentColor"/></svg>arlo.penhallow@meridelkestrova.com</li>
    <li><svg viewBox="0 0 10 10"><circle cx="5" cy="5" r="4.4" fill="none" stroke="currentColor"/><path d="M.6 5h8.8M5 .6c-2.4 2.4-2.4 6.4 0 8.8M5 .6c2.4 2.4 2.4 6.4 0 8.8" fill="none" stroke="currentColor" stroke-width=".8"/></svg>meridelkestrova.com</li>
  </ul>
  <div class="card__mark wordmark">Meridel<br>Kestrova</div>
</section>

<!-- Light card front -->
<section class="card card--light card--f2" aria-label="Business card front, light">
  <div class="card__edge card__edge--left"></div>
  <div class="card__edge card__edge--right"></div>
  <div class="card__logo-centre wordmark">Meridel Kestrova</div>
  <ul class="card__services"><li>Business Service</li><li>Business Service</li><li>Business Service</li></ul>
  <div class="card__baseline"></div>
</section>

<!-- Light card back -->
<section class="card card--light card--b2" aria-label="Business card back, light">
  <div class="card__logo-small wordmark">Meridel<br>Kestrova</div>
  <div class="card__name">Arlo Penhallow</div>
  <svg class="card__role-bar" viewBox="0 0 400 16" preserveAspectRatio="none" aria-hidden="true">
    <polygon points="0,0 150,0 160,8 150,16 0,16" fill="var(--teal)"/>
    <rect x="160" y="7" width="240" height="1.5" fill="var(--teal)"/>
  </svg>
  <div class="card__role" style="color:#fff">Director</div>
  <ul class="card__contacts">
    <li class="gap"><svg viewBox="0 0 10 10"><path d="M5 0C3 0 1.6 1.5 1.6 3.3 1.6 6 5 10 5 10s3.4-4 3.4-6.7C8.4 1.5 7 0 5 0zm0 4.6a1.3 1.3 0 110-2.6 1.3 1.3 0 010 2.6z" fill="currentColor"/></svg>17 Wendle St, Corvath Vale, NSW 2100</li>
    <li><svg viewBox="0 0 10 10"><rect x="2.5" y="0" width="5" height="10" rx="1" fill="currentColor"/></svg>+61 2 8150 4417</li>
    <li><svg viewBox="0 0 10 10"><path d="M2 0l2 2.5-1 1.2c.7 1.4 1.8 2.5 3.2 3.2l1.2-1L10 8 8.6 10C4 9.4.6 6 0 1.4z" fill="currentColor"/></svg>+61 455 302 918</li>
    <li><svg viewBox="0 0 10 10"><rect x="0" y="2" width="10" height="6.5" fill="none" stroke="currentColor"/><path d="M0 2l5 3.5L10 2" fill="none" stroke="currentColor"/></svg>arlo.penhallow@meridelkestrova.com</li>
    <li><svg viewBox="0 0 10 10"><circle cx="5" cy="5" r="4.4" fill="none" stroke="currentColor"/><path d="M.6 5h8.8M5 .6c-2.4 2.4-2.4 6.4 0 8.8M5 .6c2.4 2.4 2.4 6.4 0 8.8" fill="none" stroke="currentColor" stroke-width=".8"/></svg>meridelkestrova.com</li>
  </ul>
  <div class="card__mark wordmark">Meridel<br>Kestrova</div>
</section>

</body>
</html>
```